Business Card Design for Consulting Company

I require a Business Card design for my Consulting company. <br/><br/>My company name is: Marek Olvani Consulting Inc.<br/>My website is: www.marekolvaniconsulting.example<br/><br/>My company focuses on management and software development for the Tallobrix CRM platform (www.tallobrix.example)<br/><br/>I have a logo already designed...see attached.
Updates

Also Include my Name and Title: Marek T.L. Olvani President

Target Market(s)

Tallobrix Customers

Contact Information for Business Card

Only include my LOGO (provided)
My Name: Marek TL Olvani
My Title: President
My Company Name: Marek Olvani Consulting Inc.
My Website: www.marekolvaniconsulting.example
My Email: marek.olvani.consulting@mailbox.example

NO PHONE NUMBER
NO ADDRESS

Font styles to use
Serif
Sans Serif
Other font styles liked:
• see my website: www.marekolvaniconsulting.example

Colors

Designer to choose colors to be used in the design.

Requirements
Must have
• Must include my Orange
• Include my name (Marek T.L. Olvani), title (President) company name, website and email
• It should also have a tag line like: Tallobrix Consulting
• I'm flexible with the tag line
Should not have
• Don't include my phone number or address

```html
<!DOCTYPE html>
<html lang="en">
<head>
<meta charset="utf-8">
<title>Marek Olvani Consulting Inc. — Business Card</title>
<link rel="stylesheet" href="https://fonts.googleapis.com/css2?family=Michroma&family=Open+Sans:wght@400;600;700&display=swap">
<style>
  :root {
    --backdrop: #1c1c1d;
    --card-dark: #231f20;
    --brand-orange: #f5821f;
    --ink-light: #ffffff;
    --ink-dark: #231f20;
  }
  * { margin: 0; padding: 0; box-sizing: border-box; }
  html, body { width: 1200px; height: 900px; overflow: hidden; }
  body {
    background: var(--backdrop);
    font-family: "Open Sans", Arial, sans-serif;
    display: flex;
    flex-direction: column;
    align-items: center;
    justify-content: center;
    gap: 40px;
  }
  .card {
    position: relative;
    width: 700px;
    height: 400px;
    background: var(--brand-orange);
    overflow: hidden;
    box-shadow: 0 10px 30px rgba(0,0,0,0.45);
  }
  .card-shape { position: absolute; inset: 0; }
  .brand-mark {
    position: absolute;
    display: flex;
    align-items: center;
    gap: 14px;
    color: var(--brand-orange);
    font-weight: 700;
    white-space: nowrap;
  }
  .brand-square {
    width: 26px;
    height: 26px;
    background: var(--brand-orange);
  }
  /* front */
  .card-front .brand-mark {
    left: 50%; top: 110px;
    transform: translateX(-50%);
    font-size: 42px;
  }
  .tagline {
    position: absolute;
    left: 0; right: 0;
    top: 300px;
    text-align: center;
    font-size: 22px;
    font-weight: 600;
    color: var(--ink-dark);
  }
  /* back */
  .card-back .brand-mark {
    left: 50%; top: 50px;
    transform: translateX(-50%);
    font-size: 34px;
  }
  .company-name {
    position: absolute;
    left: 0; right: 0; top: 108px;
    text-align: center;
    font-size: 13px;
    font-weight: 700;
    letter-spacing: 0.5px;
    color: var(--ink-light);
    text-transform: uppercase;
  }
  .person {
    position: absolute;
    left: 36px; top: 268px;
  }
  .person-name {
    font-family: "Michroma", Arial, sans-serif;
    font-size: 19px;
    color: var(--brand-orange);
    text-transform: uppercase;
    letter-spacing: 0.5px;
    white-space: nowrap;
  }
  .person-title {
    margin-top: 4px;
    font-size: 17px;
    font-weight: 600;
    color: var(--ink-light);
  }
  .contact {
    position: absolute;
    right: 24px; top: 200px;
    list-style: none;
    text-align: right;
    font-size: 14px;
    font-weight: 600;
    line-height: 1.45;
    color: var(--ink-light);
    white-space: nowrap;
  }
</style>
</head>
<body>

<section class="card card-front" aria-label="Business card front">
  <svg class="card-shape" viewBox="0 0 700 400" aria-hidden="true">
    <path d="M14 0 H700 V290 H64 Q14 290 14 340 V0 Z" fill="var(--card-dark)"/>
  </svg>
  <div class="brand-mark"><span class="brand-square"></span>Marek Olvani</div>
  <p class="tagline">Tallobrix Consulting</p>
</section>

<section class="card card-back" aria-label="Business card back">
  <svg class="card-shape" viewBox="0 0 700 400" aria-hidden="true">
    <path d="M14 0 H700 V170 H380 Q330 170 330 220 V350 H14 Z" fill="var(--card-dark)"/>
  </svg>
  <div class="brand-mark"><span class="brand-square"></span>Marek Olvani</div>
  <p class="company-name">Marek Olvani Consulting Inc.</p>
  <div class="person">
    <p class="person-name">Marek TL Olvani</p>
    <p class="person-title">President</p>
  </div>
  <ul class="contact">
    <li>www.marekolvaniconsulting.example</li>
    <li>marek.olvani.consulting@mailbox.example</li>
  </ul>
</section>

</body>
</html>
```